Website Design Brief – B2B Industrial Engineering Company

DO NOT CONTACT ME PRIVATELY. ANY INQUIRES WILL BE IGNORED.

1. Industry & Company Background

We are a Swiss B2B engineering and manufacturing company operating in the fields of:
• Industrial air technology (Lufttechnik)
• Metal fabrication and plant construction (Metallbau / Anlagebau)
• Design, fabrication, installation, maintenance, and servicing of:
• Spray booths / paint booths
• Extraction and ventilation systems
• Filtration and environmentally efficient air-handling systems

We plan, build, manufacture, sell, install, and maintain these systems.
Most systems are custom-built in-house (metalwork, apparatus construction, air technology), tailored to customer requirements rather than relying only on standard components.

We are a family-run business with a strong focus on:
• Swiss quality
• Long-term experience
• Reliability and engineering competence
• Environmental efficiency
• Apprenticeship training (we train apprentices in our workshop)

2. Goal of the New Website

The new website should be a modernized evolution of our existing site, not a complete reinvention.

Key objectives:
• Look more modern, fresh, and dynamic
• Clearly communicate our experience, quality, and values
• Emphasize Swiss engineering, tradition, and reliability
• Feel professional and trustworthy, not flashy
• Be clean, uncluttered, and highly structured
• Encourage visitors to submit an inquiry or contact us

The website should feel confident and industrial-premium, with a strong focus on clarity and usability.

3. Overall Design Direction

Visual Style
• Modern industrial design
• Clean layouts with strong structure
• Clear visual hierarchy
• Balanced use of whitespace
• Calm, confident, engineering-focused look

Layout Principles (Important)
• Use clearly separated sections
• Avoid overlapping elements
• Avoid overly complex or experimental layouts
• Prefer grid-based, structured compositions
• Each section should have a clear start and end
• Designs should translate well into standard web layouts without reliance on floating or layered effects

Motion & Media
• A video header on the homepage is strongly desired
• Industrial footage, workshop, fabrication, systems in operation, or environmental technology
• Subtle animations are welcome (e.g., fades, simple transitions)
• Avoid heavy parallax or effects that depend on overlapping elements

4. Target Audience
• Industrial and B2B clients
• Engineers, facility managers, workshop owners
• Decision-makers looking for reliable long-term partners
• Customers who value custom solutions, quality, and service

5. Reference Website

Existing website (content & structure reference):
https://www.glanzhallenwerk.ch

This site:
• Provides existing branding, colors, and tone
• Is the baseline for content and structure
• Should be visually improved, simplified, and modernized

6. Pages to Design (Initial Phase – 5 Pages)

Please design 5 key pages, based on the existing website structure:
1. Home
• Video header
• Clear value proposition
• Overview of services
• Trust elements (experience, Swiss quality, family business)
• Strong call-to-action (Contact / Request Quote)
2. Company / About Us
• Company history
• Values and philosophy
• Swiss quality and tradition
• Family business
• Apprenticeship training and workshop
3. Services / Solutions
• Planning
• Manufacturing
• Installation
• Maintenance & service
• Custom systems vs standard components
4. Products / Systems
• Spray booths
• Extraction systems
• Filtration and air technology
• Modular but clearly structured sections
5. Contact
• Contact form
• Company details
• Location
• Clear inquiry-focused layout

7. Functional Requirements

Must Have
• Contact form
• Newsletter signup
• Cookie consent (EU / GDPR compliant)
• Privacy policy and legal pages (EU data protection)
• Clear navigation structure
• PDF catalog download area (well organized)

Must NOT Have
• No search feature
• No cluttered mega-menus
• No hidden or confusing navigation

8. Future Expansion (Phase Two – Not Required Now)

Designs should allow future expansion, including:
• Multi-language support (English, French, Italian)
• Optional webshop integration
• Expanded product catalog
• Additional service pages

These features do not need to be designed now, but the layout should be flexible enough to support them later.

9. Colors & Branding
• Use colors similar to the existing website
• Industrial, neutral tones preferred
• Accents should feel technical and professional
• Avoid trendy or overly bright color palettes

10. Tone & Messaging

The design should communicate:
• Experience
• Precision
• Trust
• Environmental responsibility
• Custom engineering capability
• Long-term partnership mindset

The overall impression should be:

“A modern Swiss engineering company with deep experience, strong values, and reliable solutions.”

11. Final Notes for Designers
• Focus on clarity, structure, and usability
• Designs should be realistic to implement with standard web layouts
• Avoid designs that rely on overlapping elements or complex layering
• Think in terms of clean sections, strong grids, and clear content flow
• The primary conversion goal is customer inquiries

Target Market(s)

The target market is B2B industrial customers, not consumers.

Industry/Entity Type

B2B industrial engineering and manufacturing (air technology, metal construction, plant engineering).

Number of Pages Required

5+ page

Requirements
Must have
• Clean structured layout, clear B2B positioning, video header, strong inquiry CTA, contact form, GDPR compliance, PDF downloads.
Nice to have
• Newsletter signup, multilingual-ready structure, future webshop support.
Should not have
• Search feature, overlapping elements, complex layered layouts, cluttered navigation.

```html
<!DOCTYPE html>
<html lang="en">
<head>
<meta charset="utf-8">
<title>Ventaro Systems AG – Industrial Air Technology</title>
<link rel="stylesheet" href="https://fonts.googleapis.com/css2?family=Catamaran:wght@500;600;700&family=Montserrat:wght@400;500;600;700&display=swap">
<style>
:root{
  --blue:#1b9ad8;
  --blue-dark:#0f7fbf;
  --navy:#2b3c5e;
  --navy-deep:#25344f;
  --ink:#111a2b;
  --text:#4d5565;
  --muted:#8a92a0;
  --light:#f4f6f9;
  --line:#e3e7ee;
  --white:#ffffff;
}
*{box-sizing:border-box;margin:0;padding:0}
html,body{width:1200px;height:4786px;overflow:hidden}
body{font-family:"Montserrat",sans-serif;color:var(--text);background:var(--white);position:relative}
.abs{position:absolute}
h1,h2,h3{font-family:"Catamaran",sans-serif;color:var(--ink);font-weight:600}
.eyebrow{font-size:15px;letter-spacing:6px;color:var(--blue);font-weight:600;text-transform:uppercase}
.btn{display:inline-flex;align-items:center;gap:12px;background:var(--blue);color:#fff;border-radius:30px;font-weight:600;font-size:14px;padding:0 8px 0 22px;height:48px}
.btn .dot{width:28px;height:28px;border-radius:50%;background:#fff;display:flex;align-items:center;justify-content:center}
.dot svg{width:12px;height:12px}
.photo{position:absolute}

/* hero */
.hero{left:0;top:0;width:1200px;height:631px;background:linear-gradient(100deg,#1f4f86 0%,#3b6b9c 45%,#7d9ab8 75%,#5a7896 100%)}
.hero .photo{right:0;top:200px;width:720px;height:431px;background:linear-gradient(180deg,rgba(160,180,200,.0) 0%,#6f8aa6 60%,#4e6a8a 100%)}
.logo{display:flex;align-items:center;gap:10px}
.logo .mark{width:30px;height:30px;border-radius:50%;background:var(--blue)}
.logo .name{font-weight:600;font-size:16px;color:#fff;line-height:1.1}
.logo .sub{font-size:10px;color:#d6e4f2}
.nav{left:93px;top:24px;width:1014px;height:50px;display:flex;align-items:center}
.nav .links{display:flex;gap:26px;margin-left:160px;font-size:12px;color:#e6eef7}
.nav .lang{margin-left:auto;font-size:12px;color:#e6eef7;margin-right:22px}
.nav .touch{border:1.5px solid #fff;border-radius:30px;height:48px;display:flex;align-items:center;gap:12px;padding:0 8px 0 20px;color:#fff;font-size:14px;font-weight:600}
.nav .touch .dot{background:var(--blue)}
.hero h1{left:93px;top:172px;color:#fff;font-size:50px;line-height:50px;font-weight:600}
.hero p{left:93px;top:310px;width:500px;color:#eef3f9;font-size:13px;line-height:24px}
.hero .cta{left:97px;top:417px}
.watch{left:310px;top:423px;display:flex;align-items:center;gap:10px;color:#fff;font-size:13px}
.watch .ring{width:36px;height:36px;border:1.5px solid #fff;border-radius:50%;display:flex;align-items:center;justify-content:center}
.notch{left:500px;top:575px}
.badge{left:553px;top:583px;width:94px;height:94px;border-radius:50%;background:var(--blue);border:4px solid #fff;display:flex;align-items:center;justify-content:center}

/* products */
.products{left:0;top:631px;width:1200px;height:845px;background:var(--light)}
.center{width:1200px;text-align:center;left:0}
.sec-title{font-size:38px;line-height:40px}
.sec-desc{font-size:13px;line-height:24px;color:var(--text)}
.card{background:#fff;border-radius:6px;width:322px;height:505px;top:884px;box-shadow:0 2px 10px rgba(20,40,70,.05);text-align:center}
.card .photo{left:8px;top:0;width:306px;height:210px;border-radius:4px}
.card .icon{position:absolute;left:122px;top:168px;width:78px;height:78px;border-radius:50%;background:var(--blue);border:5px solid #fff;display:flex;align-items:center;justify-content:center}
.card h3{position:absolute;top:262px;left:0;width:100%;font-size:22px;line-height:26px;text-transform:uppercase;font-weight:600}
.card p{position:absolute;top:330px;left:30px;width:262px;font-size:12.5px;line-height:21px;color:var(--text)}
.card .more{position:absolute;top:460px;left:0;width:100%;display:flex;justify-content:center;align-items:center;gap:10px;font-size:13px;font-weight:500;color:var(--ink)}
.mini{width:24px;height:24px;border-radius:50%;background:var(--blue);display:inline-flex;align-items:center;justify-content:center}
.mini svg{width:10px;height:10px}

/* about */
.about-title{left:100px;top:1590px;font-size:38px;font-family:"Catamaran",sans-serif}
.about p{width:440px;font-size:13px;line-height:24px}
.years{left:740px;top:1695px;width:112px;height:112px;border-radius:50%;background:var(--blue);border:6px solid #fff;color:#fff;display:flex;align-items:center;justify-content:center;font-size:30px;font-weight:600;font-family:"Catamaran",sans-serif}

/* credentials */
.creds{left:0;top:2035px;width:1200px;height:740px;background:var(--navy)}
.stat{top:2265px;width:218px;height:196px;background:#fff;border-radius:4px;border-bottom:6px solid var(--blue);text-align:center}
.stat .big{font-family:"Catamaran",sans-serif;font-size:42px;font-weight:600;color:#333c4c;margin-top:36px;line-height:44px}
.stat .lbl{font-size:14px;color:var(--text);margin-top:12px}
.stat .acc{font-size:12px;color:var(--blue);margin-top:16px;line-height:20px;text-transform:uppercase}
.stat .cert{font-size:12px;font-weight:600;color:#333c4c;display:flex;justify-content:center;align-items:center;gap:6px}
.docs{left:133px;top:2512px;width:933px;height:137px;border:1.5px solid #4e6fa3;border-radius:10px;background:#34497a}
.docs h3{position:absolute;left:48px;top:38px;color:#fff;font-family:"Montserrat",sans-serif;font-size:17px;font-weight:600}
.docs p{position:absolute;left:48px;top:72px;width:370px;color:#c9d3e4;font-size:12.5px;line-height:24px}
.pill{position:absolute;top:46px;height:46px;border-radius:30px;display:flex;align-items:center;gap:10px;padding:0 20px 0 8px;font-size:13px;color:#fff}
.pill .ic{width:30px;height:30px;border-radius:50%;display:flex;align-items:center;justify-content:center}

/* consult */
.consult-photo{left:0;top:3060px;width:1200px;height:437px;background:linear-gradient(180deg,#ffffff 0%,#cfd8e2 30%,#a8b4c2 60%,#6f7c8c 100%)}

/* testimonials */
.arrow-btn{top:3602px;width:40px;height:40px;border:1.5px solid var(--line);border-radius:50%;display:flex;align-items:center;justify-content:center}
.quote{top:3680px;width:314px;height:425px;border:1px solid var(--line);border-radius:4px;background:#fff}
.quote .q{position:absolute;left:40px;top:38px}
.quote p{position:absolute;left:40px;top:78px;width:236px;font-size:12.5px;line-height:24.5px;color:var(--text)}
.quote .rule{position:absolute;left:40px;top:355px;width:236px;border-top:1px solid var(--line)}
.quote .who{position:absolute;left:40px;top:362px;font-size:13px;font-weight:600;color:var(--ink)}
.quote .role{position:absolute;left:40px;top:386px;font-size:11px;color:var(--muted);text-transform:uppercase}
.quote .org{position:absolute;left:40px;top:404px;font-size:9px;color:#a6adb8}

/* footer */
.footer{left:0;top:4210px;width:1200px;height:576px;background:var(--navy)}
.foot-col h4{font-size:17px;font-weight:600;color:#fff;letter-spacing:.5px;margin-bottom:30px}
.foot-col li{list-style:none;font-size:13px;color:#d2dae7;margin-bottom:17px;display:flex;gap:6px;align-items:flex-start;line-height:20px}
</style>
</head>
<body>

<!-- HERO -->
<section class="hero abs">
  <div class="photo" role="img" aria-label="Industrial rooftop air handling units with ducting under a blue sky"></div>
  <div class="nav abs">
    <div class="logo">
      <span class="mark"></span>
      <div><div class="name">Ventaro Systems AG</div><div class="sub">Industrial Air Technology</div></div>
    </div>
    <div class="links"><span>Systems</span><span>Technical Inquiry</span><span>Documentation</span><span>Support</span></div>
    <div class="lang">◍ En ▾</div>
    <div class="touch">Get In Touch <span class="dot"><svg viewBox="0 0 12 12"><path d="M3 9L9 3M4 3h5v5" stroke="#fff" stroke-width="1.6" fill="none"/></svg></span></div>
  </div>
  <h1 class="abs">Engineered Air Technology Systems<br>for Industrial Environments</h1>
  <p class="abs">Design, manufacturing, and lifecycle support for industrial air handling, filtration, and process extraction systems. Engineered for regulatory compliance and continuous operation.</p>
  <div class="btn abs cta">Technical Inquiry <span class="dot"><svg viewBox="0 0 12 12"><path d="M3 9L9 3M4 3h5v5" stroke="#1b9ad8" stroke-width="1.6" fill="none"/></svg></span></div>
  <div class="watch abs"><span class="ring"><svg width="10" height="12" viewBox="0 0 10 12"><path d="M1 1l8 5-8 5z" fill="#fff"/></svg></span>Watch intro video</div>
</section>
<svg class="notch abs" width="200" height="60" viewBox="0 0 200 60"><path d="M0 56 C50 56 60 20 100 20 C140 20 150 56 200 56 L200 60 L0 60Z" fill="#f4f6f9"/></svg>
<div class="badge abs"><svg width="26" height="26" viewBox="0 0 12 12"><path d="M3 9L9 3M4 3h5v5" stroke="#fff" stroke-width="1.3" fill="none"/></svg></div>

<!-- PRODUCTS -->
<section class="products abs"></section>
<div class="abs center eyebrow" style="top:722px">Products</div>
<h2 class="abs center sec-title" style="top:748px">System Categories</h2>
<p class="abs center sec-desc" style="top:808px">Engineered systems for industrial air technology applications. Designed<br>for compliance, efficiency, and long-term operational stability.</p>

<article class="card abs" style="left:93px">
  <div class="photo" role="img" aria-label="Spray gun applying coating inside a paint booth" style="background:linear-gradient(160deg,#5e7a96,#a9bccd 60%,#d5dee8)"></div>
  <div class="icon"><svg width="28" height="28" viewBox="0 0 24 24" fill="none" stroke="#fff" stroke-width="1.6"><rect x="8" y="9" width="6" height="12" rx="1"/><path d="M10 9V6h2v3M15 5h2M16 8h3M15 11h2"/></svg></div>
  <h3>Spray Booth &amp;<br>Coating Systems</h3>
  <p>Enclosed industrial painting systems engineered for controlled airflow, filtration efficiency, and regulatory compliance in industrial coating processes.</p>
  <div class="more">View System Details <span class="mini"><svg viewBox="0 0 12 12"><path d="M3 9L9 3M4 3h5v5" stroke="#fff" stroke-width="1.8" fill="none"/></svg></span></div>
</article>
<article class="card abs" style="left:438px">
  <div class="photo" role="img" aria-label="Extraction pipework and valves in a process plant" style="background:linear-gradient(160deg,#2f5f8e,#7fa8c8 55%,#c9a574)"></div>
  <div class="icon"><svg width="28" height="28" viewBox="0 0 24 24" fill="none" stroke="#fff" stroke-width="1.6"><rect x="4" y="4" width="16" height="16" rx="2"/><circle cx="12" cy="12" r="4"/></svg></div>
  <h3>Extraction &amp;<br>Capture Systems</h3>
  <p>Extraction systems designed for targeted capture of fumes, dust, and process emissions, ensuring workplace safety and stable production conditions.</p>
  <div class="more">View System Architecture <span class="mini"><svg viewBox="0 0 12 12"><path d="M3 9L9 3M4 3h5v5" stroke="#fff" stroke-width="1.8" fill="none"/></svg></span></div>
</article>
<article class="card abs" style="left:788px">
  <div class="photo" role="img" aria-label="Ceiling-mounted air handling units in an industrial hall" style="background:linear-gradient(170deg,#1d4f8a,#5f8dc0 55%,#a5c2df)"></div>
  <div class="icon"><svg width="28" height="28" viewBox="0 0 24 24" fill="none" stroke="#fff" stroke-width="1.6"><path d="M6 4l10 2v14L6 18z"/><path d="M9 9h4M9 12h4M9 15h4"/></svg></div>
  <h3>Air Handling &amp;<br>Filtration Systems</h3>
  <p>Integrated air handling units for ventilation, filtration, and climate control, optimized for continuous industrial operation and energy efficiency.</p>
  <div class="more">Explore Air Technology <span class="mini"><svg viewBox="0 0 12 12"><path d="M3 9L9 3M4 3h5v5" stroke="#fff" stroke-width="1.8" fill="none"/></svg></span></div>
</article>

<!-- ABOUT -->
<section class="about">
  <div class="abs eyebrow" style="left:100px;top:1562px">About Us</div>
  <h2 class="abs about-title">Swiss Family Business.</h2>
  <p class="abs" style="left:100px;top:1655px">For over 35 years, we've been delivering custom-engineered solutions in industrial air technology and metal fabrication. As a Swiss family-run company, we combine traditional craftsmanship with modern engineering.</p>
  <p class="abs" style="left:100px;top:1765px">From planning to manufacturing, installation, and maintenance – everything from a single source. We don't offer standard products; we create tailored solutions that meet your exact requirements.</p>
  <div class="btn abs" style="left:95px;top:1898px;height:46px">Learn More <span class="dot"><svg viewBox="0 0 12 12"><path d="M3 9L9 3M4 3h5v5" stroke="#1b9ad8" stroke-width="1.6" fill="none"/></svg></span></div>
  <div class="photo" role="img" aria-label="Workshop with stainless ductwork and an industrial fan" style="left:598px;top:1565px;width:196px;height:300px;background:linear-gradient(160deg,#cfd4da,#8d959f 60%,#5c636d)"></div>
  <div class="photo" role="img" aria-label="Plant hall with ducts lit by warm sunlight" style="left:808px;top:1602px;width:290px;height:344px;background:linear-gradient(160deg,#2c5d95,#c4855a 35%,#3f79b3 70%,#1c4d86)"></div>
  <div class="years abs">38</div>
</section>

<!-- CREDENTIALS -->
<section class="creds abs"></section>
<div class="abs center eyebrow" style="top:2097px">Technical Documentation</div>
<h2 class="abs center sec-title" style="top:2126px;color:#fff">Technical Credentials</h2>
<p class="abs center sec-desc" style="top:2186px;color:#e2e8f2">Engineering expertise and operational capability for industrial air<br>technology systems.</p>

<div class="stat abs" style="left:133px"><div class="big">35+</div><div class="lbl">Years of operation</div><div class="acc">Since 1991</div></div>
<div class="stat abs" style="left:372px"><div class="big">100%</div><div class="lbl">In-house manufacturing</div><div class="acc">Swiss production<br>facility</div></div>
<div class="stat abs" style="left:610px">
  <div class="cert" style="margin-top:42px"><svg width="14" height="14" viewBox="0 0 14 14"><circle cx="7" cy="7" r="6" fill="none" stroke="#1b9ad8" stroke-width="1.3"/><path d="M4 7l2 2 4-4" stroke="#1b9ad8" stroke-width="1.3" fill="none"/></svg>ISO 9001:2015</div>
  <div class="acc" style="margin-top:8px">Quality management</div>
  <div class="cert" style="margin-top:26px"><svg width="14" height="14" viewBox="0 0 14 14"><circle cx="7" cy="7" r="6" fill="none" stroke="#1b9ad8" stroke-width="1.3"/><path d="M4 7l2 2 4-4" stroke="#1b9ad8" stroke-width="1.3" fill="none"/></svg>EN 16282</div>
  <div class="acc" style="margin-top:8px">Ventilation compliance</div>
</div>
<div class="stat abs" style="left:848px"><div class="big">24/7</div><div class="lbl">Lifecycle support</div><div class="acc">Service &amp; maintenance</div></div>

<div class="docs abs">
  <h3>TECHNICAL DOCUMENTATION</h3>
  <p>System specifications, compliance certificates, and technical drawings available for download.</p>
  <div class="pill" style="left:506px;background:#5aa5ea"><span class="ic" style="background:#fff"><svg width="14" height="14" viewBox="0 0 14 14" fill="none" stroke="#5aa5ea" stroke-width="1.5"><path d="M7 2v7M4 6l3 3 3-3M3 12h8"/></svg></span>System Catalog PDF</div>
  <div class="pill" style="left:727px;border:1.5px solid #6f8fc2"><span class="ic" style="background:#5aa5ea"><svg width="14" height="14" viewBox="0 0 14 14" fill="none" stroke="#fff" stroke-width="1.3"><rect x="3" y="2" width="8" height="10" rx="1"/><path d="M5 5h4M5 8h4"/></svg></span>Compliance Docs</div>
</div>

<!-- CONSULTATION -->
<div class="consult-photo abs" role="img" aria-label="Row of rooftop condenser units with insulated pipework under a cloudy sky"></div>
<div class="abs center eyebrow" style="top:2864px">Request a Consultation</div>
<h2 class="abs center" style="top:2886px;font-size:54px;line-height:60px">Request Technical Consultation</h2>
<p class="abs center sec-desc" style="top:2968px">Discuss your application requirements with our engineering team. Submit system parameters<br>and operational specifications for technical evaluation.</p>
<div class="abs" style="left:0;width:1200px;top:3046px;display:flex;justify-content:center"><div class="btn">Submit System Requirements <span class="dot"><svg viewBox="0 0 12 12"><path d="M3 9L9 3M4 3h5v5" stroke="#1b9ad8" stroke-width="1.6" fill="none"/></svg></span></div></div>

<!-- TESTIMONIALS -->
<div class="abs eyebrow" style="left:100px;top:3564px">Testimonials</div>
<h2 class="abs sec-title" style="left:100px;top:3594px">Client References</h2>
<div class="arrow-btn abs" style="left:1016px"><svg width="10" height="10" viewBox="0 0 10 10"><path d="M6 2L3 5l3 3" stroke="#1b9ad8" fill="none" stroke-width="1.4"/></svg></div>
<div class="arrow-btn abs" style="left:1066px"><svg width="10" height="10" viewBox="0 0 10 10"><path d="M4 2l3 3-3 3" stroke="#1b9ad8" fill="none" stroke-width="1.4"/></svg></div>

<article class="quote abs" style="left:100px">
  <svg class="q" width="26" height="20" viewBox="0 0 26 20"><path d="M0 10h10v10H0zM0 10C0 4 4 0 10 0v4C6 4 4 6 4 10zM14 10h10v10H14zM14 10c0-6 4-10 10-10v4c-4 0-6 2-6 6z" fill="#1b9ad8"/></svg>
  <p>The extraction system has maintained 99.2% capture efficiency over 18 months of continuous operation. Downtime has been reduced by 40% compared to our previous installation. Filter maintenance intervals meet specifications and operational costs align with projected figures.</p>
  <div class="rule"></div>
  <div class="who">Lukas Brenner</div><div class="role">Plant Manager</div><div class="org">Alpen Surface Coatings GmbH</div>
</article>
<article class="quote abs" style="left:443px">
  <svg class="q" width="26" height="20" viewBox="0 0 26 20"><path d="M0 10h10v10H0zM0 10C0 4 4 0 10 0v4C6 4 4 6 4 10zM14 10h10v10H14zM14 10c0-6 4-10 10-10v4c-4 0-6 2-6 6z" fill="#1b9ad8"/></svg>
  <p>System commissioning was completed within the planned timeframe. The air handling unit operates at specified parameters with measured energy consumption 12% below initial projections. Control system integration with our facility management platform functioned as documented.</p>
  <div class="rule"></div>
  <div class="who">Dr. Stefan Imhof</div><div class="role">Facility Operations Manager</div><div class="org">Limmat Life Science Institute</div>
</article>
<article class="quote abs" style="left:786px">
  <svg class="q" width="26" height="20" viewBox="0 0 26 20"><path d="M0 10h10v10H0zM0 10C0 4 4 0 10 0v4C6 4 4 6 4 10zM14 10h10v10H14zM14 10c0-6 4-10 10-10v4c-4 0-6 2-6 6z" fill="#1b9ad8"/></svg>
  <p>The spray booth system passed regulatory inspection on first submission. Airflow uniformity measurements confirmed design specifications. Filter life exceeds manufacturer estimates by 15%. Technical support response times average under 4 hours for all service requests.</p>
  <div class="rule"></div>
  <div class="who">Reto Gisler</div><div class="role">Plant Manager</div><div class="org">Alpen Surface Coatings GmbH</div>
</article>

<!-- FOOTER -->
<footer class="footer abs"></footer>
<svg class="abs" style="left:0;top:4210px" width="600" height="146" viewBox="0 0 600 146"><path d="M0 0H540C480 0 470 146 380 146H0Z" fill="#fff"/></svg>
<div class="logo abs" style="left:100px;top:4250px">
  <span class="mark" style="width:48px;height:48px"></span>
  <div><div class="name" style="color:var(--ink);font-size:25px">Ventaro Systems AG</div><div class="sub" style="color:var(--ink);font-size:16px;margin-top:4px">Industrial Air Technology</div></div>
</div>
<div class="abs" style="left:600px;top:4245px;color:#fff;font-size:16px;font-weight:600">Technical Updates</div>
<div class="abs" style="left:600px;top:4273px;color:#d2dae7;font-size:11px">Receive system updates and technical documentation.</div>
<div class="abs" style="left:600px;top:4305px;width:500px;height:48px;background:#fff;border-radius:30px;display:flex;align-items:center;padding:0 4px 0 20px">
  <span style="font-size:10px;color:#a6adb8">Enter Email Address...</span>
  <span class="btn" style="margin-left:auto;height:40px;font-size:14px;padding:0 6px 0 18px">Subscribe <span class="dot" style="width:26px;height:26px"><svg viewBox="0 0 12 12"><path d="M3 9L9 3M4 3h5v5" stroke="#1b9ad8" stroke-width="1.6" fill="none"/></svg></span></span>
</div>

<div class="foot-col abs" style="left:100px;top:4462px"><h4>SYSTEM CATEGORIES</h4><ul><li>Spray &amp; Painting Systems</li><li>Extraction &amp; Capture Systems</li><li>Air Handling &amp; Filtration</li></ul></div>
<div class="foot-col abs" style="left:375px;top:4462px"><h4>TECHNICAL RESOURCES</h4><ul><li><span style="color:var(--blue)">⤓</span>Spray &amp; Painting Systems</li><li><span style="color:var(--blue)">⤓</span>Compliance Documentation</li><li><span style="color:var(--blue)">⤓</span>Technical Drawings</li></ul></div>
<div class="foot-col abs" style="left:657px;top:4462px"><h4>COMPANY</h4><ul><li>Technical Inquiry</li><li>Lifecycle Support</li><li>System Catalog</li></ul></div>
<div class="foot-col abs" style="left:863px;top:4462px;width:240px"><h4>CONTACT</h4><ul>
  <li style="margin-top:-10px"><svg width="12" height="14" viewBox="0 0 12 14" style="margin-top:3px;flex:none"><path d="M6 13S1 8 1 5a5 5 0 0110 0c0 3-5 8-5 8z" fill="none" stroke="#1b9ad8" stroke-width="1.2"/><circle cx="6" cy="5" r="1.6" fill="#1b9ad8"/></svg><span>Halvetra Engineering AG<br>Werkstrasse 17 8048 Zürich, Switzerland</span></li>
  <li><svg width="12" height="12" viewBox="0 0 12 12" style="margin-top:4px;flex:none"><path d="M2 1l2 0 1 3-1.5 1a7 7 0 003.5 3.5L8 7l3 1v2c0 .6-.5 1-1 1C5 11 1 7 1 2c0-.5.4-1 1-1z" fill="none" stroke="#1b9ad8" stroke-width="1.1"/></svg>+41 44 555 01 90</li>
  <li><svg width="12" height="10" viewBox="0 0 12 10" style="margin-top:5px;flex:none"><rect x=".6" y=".6" width="10.8" height="8.8" rx="1" fill="none" stroke="#1b9ad8" stroke-width="1.1"/><path d="M1 1l5 4 5-4" fill="none" stroke="#1b9ad8" stroke-width="1.1"/></svg>info@halvetra-engineering.ch</li>
</ul></div>

<div class="abs" style="left:100px;top:4733px;width:1000px;border-top:1px solid #4b5d80"></div>
<div class="abs" style="left:97px;top:4752px;font-size:11px;color:#d2dae7">© 2026 Ventaro Systems AG. Zurich, Switzerland.</div>
<div class="abs" style="left:712px;top:4752px;font-size:11px;color:#d2dae7">Privacy Policy &nbsp;/&nbsp; Legal Notice &nbsp;/&nbsp; Terms of Service &nbsp;/&nbsp; Cookie Settings</div>

</body>
</html>
```